Funky Business card design for starting out career counsellor - Melbourne, Australia

Hi there, I am seeking a business card design to send straight to print. I work from a psycho-spiritual framework (existential, non-dual, transpersonal) framework and was hoping for something that is modern, funky - yet has an established grounded feel to it, but pushes the edge of art and boundary. Minimal design is good.
I don't have a corporate identity other than my wordpress template at www.pathwaybrightly.com. I like the depth of the this wordpress template, with the thought provaking image. A design that aligns to the wordpress template would be awesome (but unique is okay too).
Thanks for your help :)
Contact details for card:
Marcus Halbrenn Registered Career Counsellor marcus@pathwaybrightly.com
(existential, non-dual, transpersonal)
www.pathwaybrightly.com +61 (0) 412 968 204 Melbourne CBD & Globally on Vidlink

```html
<!DOCTYPE html>
<html lang="en">
<head>
<meta charset="utf-8">
<title>Marcus Halbrenn – Business Card</title>
<link rel="stylesheet" href="https://fonts.googleapis.com/css2?family=Josefin+Slab:wght@300;400&family=Poiret+One&family=Allura&display=swap">
<style>
  :root {
    --canvas-bg: #5b5d60;
    --teal: #3b7a8c;
    --teal-deep: #347083;
    --teal-light: #5a95a6;
    --paper: #ffffff;
    --ink-grey: #4d5257;
    --sky-top: #7f93a8;
    --sky-mid: #c7a7a0;
    --sunset: #f0a35e;
    --glow: #fbd79a;
  }
  * { margin: 0; padding: 0; box-sizing: border-box; }
  html, body { width: 1200px; height: 920px; overflow: hidden; }
  body { background: var(--canvas-bg); position: relative; }

  .card {
    position: absolute;
    width: 640px;
    height: 380px;
    overflow: hidden;
    box-shadow: 0 10px 28px rgba(0,0,0,.35);
  }

  /* Front */
  .card--front { left: 70px; top: 50px; background: var(--teal); }
  .card--front .hero-image {
    position: absolute;
    left: 190px; top: 30px;
    width: 260px; height: 240px;
    background:
      linear-gradient(to right, var(--teal) 0%, rgba(59,122,140,0) 22%, rgba(59,122,140,0) 78%, var(--teal) 100%),
      linear-gradient(to bottom, var(--sky-top) 0%, var(--sky-mid) 55%, var(--sunset) 82%, var(--teal) 100%);
  }
  .card--front .tagline {
    position: absolute;
    left: 0; right: 0; top: 292px;
    text-align: center;
    font-family: "Allura", cursive;
    font-size: 40px;
    color: var(--paper);
    letter-spacing: 1px;
  }

  /* Back */
  .card--back { left: 490px; top: 490px; background: var(--teal-deep); }
  .card--back .upper { position: absolute; left: 0; top: 0; width: 100%; height: 170px; background: var(--paper); }
  .card--back .strapline-band {
    position: absolute; left: 0; top: 170px; width: 100%; height: 46px;
    background: var(--teal);
    border-bottom: 6px solid var(--teal-light);
  }
  .card--back .strapline {
    position: absolute; right: 22px; top: 176px;
    font-family: "Allura", cursive;
    font-size: 27px;
    color: var(--paper);
  }
  .portrait-ring {
    position: absolute; left: 10px; top: 80px;
    width: 216px; height: 216px; border-radius: 50%;
    background: var(--teal);
  }
  .portrait-ring .scene {
    position: absolute; left: 16px; top: 16px;
    width: 184px; height: 184px; border-radius: 50%;
    background: linear-gradient(to bottom, var(--sky-top) 0%, var(--sky-mid) 45%, var(--sunset) 75%, var(--glow) 100%);
  }
  .identity { position: absolute; right: 22px; top: 26px; text-align: right; }
  .identity .name {
    font-family: "Josefin Slab", serif;
    font-weight: 300;
    font-size: 34px;
    letter-spacing: 7px;
    color: var(--teal);
    text-transform: uppercase;
  }
  .identity .role, .identity .approach {
    font-family: "Poiret One", sans-serif;
    font-size: 17px;
    color: var(--ink-grey);
    line-height: 1.25;
  }
  .contact {
    position: absolute; right: 22px; top: 246px;
    text-align: right; list-style: none;
    font-family: "Poiret One", sans-serif;
    font-size: 17px;
    line-height: 1.45;
    color: var(--paper);
  }
</style>
</head>
<body>
  <section class="card card--front">
    <div class="hero-image" role="img" aria-label="Photo of a person leaping between cliffs against a sunset sky, seen through vertical light stripes"></div>
    <p class="tagline">Discover your authentic self...</p>
  </section>

  <section class="card card--back">
    <div class="upper"></div>
    <div class="strapline-band"></div>
    <p class="strapline">...sharing the journey of spiritual awakening</p>
    <div class="portrait-ring">
      <div class="scene" role="img" aria-label="Silhouette of a person leaping across a gap between rocks at sunset"></div>
    </div>
    <div class="identity">
      <h1 class="name">Marcus Halbrenn</h1>
      <p class="role">Registered Career Counsellor</p>
      <p class="approach">(existential, non-dual, transpersonal)</p>
    </div>
    <ul class="contact">
      <li>marcus@pathwaybrightly.com</li>
      <li>www.pathwaybrightly.com</li>
      <li>+61 (0) 412 968 204</li>
      <li>Melbourne CBD &amp; Globally on Vidlink</li>
    </ul>
  </section>
</body>
</html>
```